Thorne Legal PC business card. National Consumer Law Firm with principal office in San Francisco. We maintain additional offices in Meridian, Mississippi and Birmingham, Alabama. We protect consumers against unscrupulous mega corporations. We want to covey integrity and a willingness to take on the Goliaths of the corporate world. I like red accents. Try to use uploaded picture of Harbor Arch Span or a sketch. Licensed in California, Alabama and Mississippi. Main office: 318 Alder Ave. #407, San Francisco, CA 94110, ph. 415/555-0182, 800/555-0147 (fax), 205/555-0136 (AL).
www.thornelegalpc.example
www.claimwatch.example.
At top--Public Claim Advocacy in red. Also Thorne Legal PC at top in red. Then red horizontal line please. Or if you have another idea. I have not seen new logo.
After line on left at top
H. Dwight Thorne
Attorney
Cell 205/555-0194
dwight@thornelegalpc.example
Offices: San Francisco, CA, Birmingham, AL, Charlotte, NC and Meridian, MS

I asked that the very bottom of the BUSINESS CARD TO SAY "Offices in California, North Carolina, Alabama and Mississippi NOT STATES WHERE I AM LICENSED. I.E., I AM NOT LICENSED IN NOTH CAROLINA I NEED NEW FILES IF YOU CAN GET THEM IN THE MORNING MY TIME. WHERE CAN I FIND THE NEW FILES ONCE YOU MODIFY.

for North Carolina, I need an asterick where it is listed. "not licensed will associate counsel" AGAIN NORTH CAROLINA IS 2 WORDS WITH A SPACE BETWEEN THEM

For Biz card, put tollfree number (888)555-0129 and toll free fax (800)555-0147 somewhere like below my cell number or wherever you can. States where I have offices at the bottom: California, North Carolina, Alabama and Mississippi.

For Biz card, put tollfree number (888)555-0129 and toll free fax (800)555-0147 somewhere like below my cell number or wherever you can. States where I have offices at the bottom: California, North Carolina, Alabama and Mississippi. AstericK *North Carolina--not licensed will associate co-counel. Same with letterhead and website. I need to disclose not licensed to practice in North Carolina.

```html
<!DOCTYPE html>
<html lang="en">
<head>
<meta charset="utf-8">
<title>Thorne Legal PC – Business Card Variations</title>
<link rel="stylesheet" href="https://fonts.googleapis.com/css2?family=Open+Sans:wght@300;400&family=Roboto+Condensed:wght@400&display=swap">
<style>
  :root {
    --bg: #f1f1f1;
    --card: #ffffff;
    --ink: #1c1c1c;
    --ink-soft: #4a4a4a;
    --ink-muted: #666666;
    --accent-red: #d8231f;
    --divider: #9a9a9a;
    --sunset-top: #3b3350;
    --sunset-mid: #e0643a;
    --sunset-low: #f3a04a;
    --sunset-city: #4a3a44;
    --sky: #a9c6de;
    --sea: #2f6f98;
  }
  * { margin: 0; padding: 0; box-sizing: border-box; }
  html, body { width: 1200px; height: 418px; overflow: hidden; }
  body {
    background: var(--bg);
    font-family: "Open Sans", sans-serif;
    color: var(--ink);
    position: relative;
  }
  .card {
    position: absolute;
    top: 40px;
    width: 510px;
    height: 330px;
    background: var(--card);
    overflow: hidden;
  }
  .card--city { left: 72px; }
  .card--harbor { left: 638px; }

  .card__photo {
    position: absolute;
    left: 0; top: 0;
    width: 100%;
    height: 106px;
  }
  .card__photo--city {
    background: linear-gradient(180deg, var(--sunset-top) 0%, #8a4a55 30%, var(--sunset-mid) 55%, var(--sunset-low) 70%, var(--sunset-city) 78%, #2e2a33 100%);
  }
  .card__photo--harbor {
    background: linear-gradient(180deg, var(--sky) 0%, #c9d9e6 40%, #7fa3bf 55%, var(--sea) 70%, #24597d 100%);
  }
  .card__rule {
    position: absolute;
    left: 0; top: 106px;
    width: 100%;
    height: 6px;
    background: var(--accent-red);
  }

  .brand {
    position: absolute;
    left: 14px;
    top: 130px;
    width: 212px;
  }
  .brand__name {
    font-weight: 300;
    font-size: 21px;
    letter-spacing: 0.3px;
    color: var(--ink-soft);
    text-transform: uppercase;
    line-height: 1.2;
    white-space: nowrap;
  }
  .brand__tagline {
    margin-top: 6px;
    font-size: 14px;
    color: var(--ink);
    white-space: nowrap;
  }

  .card__divider {
    position: absolute;
    left: 234px;
    top: 120px;
    width: 2px;
    height: 172px;
    background: linear-gradient(180deg, rgba(154,154,154,0) 0%, var(--divider) 20%, var(--divider) 75%, rgba(154,154,154,0) 100%);
  }

  .person {
    position: absolute;
    left: 248px;
    right: 22px;
    top: 124px;
    text-align: right;
  }
  .person__name {
    font-family: "Roboto Condensed", sans-serif;
    font-size: 28px;
    color: var(--ink);
    text-transform: uppercase;
    text-align: left;
    white-space: nowrap;
    line-height: 1.2;
  }
  .person__title {
    margin-top: 2px;
    font-size: 15px;
  }
  .contact {
    position: absolute;
    right: 22px;
    top: 188px;
    text-align: right;
    font-size: 13px;
    line-height: 1.45;
    white-space: nowrap;
  }
  .contact__phone {
    font-size: 16px;
    margin-bottom: 1px;
  }

  .offices {
    position: absolute;
    left: 14px;
    right: 14px;
    bottom: 7px;
    text-align: center;
    white-space: nowrap;
  }
  .offices__states {
    font-size: 11.5px;
    color: var(--ink);
  }
  .offices__note {
    margin-top: 1px;
    font-size: 9.5px;
    color: var(--ink-muted);
  }
</style>
</head>
<body>

  <article class="card card--city">
    <div class="card__photo card__photo--city" role="img" aria-label="Photo of a city skyline at sunset"></div>
    <div class="card__rule"></div>
    <div class="brand">
      <div class="brand__name">Thorne Legal PC</div>
      <div class="brand__tagline">Public Claim Advocacy</div>
    </div>
    <div class="card__divider"></div>
    <div class="person">
      <div class="person__name">H. Dwight Thorne</div>
      <div class="person__title">Attorney</div>
    </div>
    <div class="contact">
      <div class="contact__phone">Cell 205/555-0194</div>
      <div>Toll free (888)555-0129</div>
      <div>Toll free fax (800)555-0147</div>
      <div>dwight@thornelegalpc.example</div>
      <div>www.thornelegalpc.example</div>
    </div>
    <div class="offices">
      <div class="offices__states">Offices in California, North Carolina*, Alabama and Mississippi</div>
      <div class="offices__note">*North Carolina – not licensed, will associate co-counsel</div>
    </div>
  </article>

  <article class="card card--harbor">
    <div class="card__photo card__photo--harbor" role="img" aria-label="Photo of the Harbor Arch Span over the bay"></div>
    <div class="card__rule"></div>
    <div class="brand">
      <div class="brand__name">Thorne Legal PC</div>
      <div class="brand__tagline">Public Claim Advocacy</div>
    </div>
    <div class="card__divider"></div>
    <div class="person">
      <div class="person__name">H. Dwight Thorne</div>
      <div class="person__title">Attorney</div>
    </div>
    <div class="contact">
      <div class="contact__phone">Cell 205/555-0194</div>
      <div>Toll free (888)555-0129</div>
      <div>Toll free fax (800)555-0147</div>
      <div>dwight@thornelegalpc.example</div>
      <div>www.thornelegalpc.example</div>
    </div>
    <div class="offices">
      <div class="offices__states">Offices in California, North Carolina*, Alabama and Mississippi</div>
      <div class="offices__note">*North Carolina – not licensed, will associate co-counsel</div>
    </div>
  </article>

</body>
</html>
```